TUMBLAVERA

We are a group of friends with a passion for ancestral knowledge of potions and medicinal formulas derived from nature. We specialise in medicinal mushrooms and adaptogens. We designed a few supplement formulas which we want to release to the market. Our team comes from biology and nutritional science background. Every product we launch will be clean in biodegradable packaging.
Our first product is a lab-tested grass-fed bovine collagen type I, II, and III mixed with organic lab-tested the most potent and bioavailable medicinal mushrooms on the market. This product will be in a pouch the print will be on the pouch or on a label, we don't know if it's possible to design a label that could be used on both? We don't know if we will be able to use organic labels yet due to the legislation changes in the UK. We are waiting for clarification.
The company is called Brindle Cove. We want to use forgotten ancestral knowledge of those potions and reintroduce them to the people. We would like our brand to look clean and friendly. A natural mix of modern and ancestral design.
Our logo and brand designs we like are attached. I have attached the source file of our logo if anyone thinks colours could be different we are open to ideas. I have also attached the visual design we were playing with on canva.com.

```html
<!DOCTYPE html>
<html lang="en">
<head>
<meta charset="utf-8">
<title>Tumblavera – Brindle Cove</title>
<link rel="stylesheet" href="https://fonts.googleapis.com/css2?family=Lobster&family=Forum&family=Poppins:wght@600&family=Archivo:wght@700&display=swap">
<style>
  :root {
    --backdrop: #d6d6d8;
    --pouch-white: #f4f4f4;
    --panel-white: #f1f1f1;
    --forest: #2b6549;
    --forest-deep: #1f5139;
    --amber: #d99a55;
    --gold: #c9a24e;
    --ink-green: #1e4d30;
    --text-white: #ffffff;
  }
  * { margin: 0; padding: 0; box-sizing: border-box; }
  html, body { width: 1200px; height: 1200px; overflow: hidden; }
  body { background: var(--backdrop); position: relative; }

  .pouch {
    position: absolute; left: 240px; top: 38px;
    width: 720px; height: 1124px;
    background: var(--panel-white);
    border-radius: 22px 22px 6px 6px;
    overflow: hidden;
  }
  .pouch__zip-strip {
    position: absolute; left: 0; top: 0; width: 100%; height: 156px;
    background: var(--pouch-white);
    border-bottom: 1px solid #e4e4e4;
  }
  .pouch__zip-line {
    position: absolute; left: 0; top: 122px; width: 100%; height: 6px;
    background: linear-gradient(#e9e9e9, #fafafa);
  }
  .brand-band { position: absolute; left: 0; top: 150px; width: 720px; height: 380px; }

  .brand {
    position: absolute; left: 0; top: 300px; width: 100%;
    display: flex; align-items: center; justify-content: center; gap: 16px;
  }
  .brand__dot { width: 34px; height: 34px; border-radius: 50%; background: var(--amber); }
  .brand__name {
    font-family: "Poppins", sans-serif; font-weight: 600;
    font-size: 58px; color: var(--amber); letter-spacing: 0.5px;
  }

  .product-title {
    position: absolute; left: 0; top: 500px; width: 100%;
    text-align: center;
    font-family: "Lobster", cursive; font-size: 104px; font-weight: 400;
    color: var(--ink-green); line-height: 1;
  }
  .product-subtitle {
    position: absolute; left: 100px; top: 614px; width: 520px;
    text-align: center;
    font-family: "Forum", serif; font-size: 27px; color: #2a2a2a;
    line-height: 1.3; padding: 4px 0;
    border-top: 2px solid #3b3b3b; border-bottom: 2px solid #3b3b3b;
  }
  .product-type {
    position: absolute; left: 0; top: 702px; width: 100%;
    text-align: center; line-height: 1.2;
    font-family: "Forum", serif; font-size: 30px; color: var(--ink-green);
  }
  .product-serving {
    position: absolute; left: 0; top: 750px; width: 100%;
    text-align: center; line-height: 1.2;
    font-family: "Forum", serif; font-size: 18px; color: var(--ink-green);
    letter-spacing: 0.5px;
  }

  .leaf-strip {
    position: absolute; left: 0; top: 962px; width: 100%; height: 84px;
    background: linear-gradient(180deg, rgba(120,175,110,0) 0%, #7fb071 30%, #4f8f55 100%);
  }
  .mushroom-art {
    position: absolute; left: 186px; top: 820px; width: 336px; height: 222px;
    background: linear-gradient(180deg, #b99d78 0%, #d6bb8e 45%, #a6875f 100%);
    border-radius: 46% 50% 18% 22% / 34% 38% 10% 10%;
  }

  .badge {
    position: absolute; top: 898px; width: 52px; height: 52px; border-radius: 50%;
    background: radial-gradient(circle, #e8cc7a 0%, var(--gold) 70%, #a9832f 100%);
  }
  .badge--a { left: 64px; }
  .badge--b { left: 122px; }
  .badge--c { left: 540px; }
  .badge--d { left: 600px; }

  .footer-band {
    position: absolute; left: 0; top: 1040px; width: 100%; height: 84px;
    background: var(--forest-deep);
    border-top: 3px solid var(--gold);
    display: flex; align-items: flex-end; justify-content: center;
    padding-bottom: 20px;
  }
  .footer-band__weight {
    font-family: "Archivo", sans-serif; font-weight: 700;
    font-size: 17px; color: var(--text-white); letter-spacing: 0.5px;
  }
</style>
</head>
<body>
  <main class="pouch">
    <div class="pouch__zip-strip"><div class="pouch__zip-line"></div></div>

    <svg class="brand-band" viewBox="0 0 720 380" aria-hidden="true">
      <defs>
        <linearGradient id="bandShade" x1="0" y1="0" x2="1" y2="0">
          <stop offset="0" stop-color="#2a6247"/>
          <stop offset="0.5" stop-color="#3b7a5d"/>
          <stop offset="1" stop-color="#2a6247"/>
        </linearGradient>
      </defs>
      <path d="M0 0 H720 V338 C560 350 420 356 360 364 C240 372 110 345 0 325 Z" fill="url(#bandShade)"/>
      <path d="M0 325 C110 345 240 372 360 364 C420 356 560 350 720 338" fill="none" stroke="#c9a24e" stroke-width="3"/>
    </svg>

    <div class="brand">
      <span class="brand__dot"></span>
      <span class="brand__name">Brindle Cove</span>
    </div>

    <h1 class="product-title">Tumblavera</h1>
    <p class="product-subtitle">Collagen Peptides &amp; Medicinal Mushrooms</p>
    <p class="product-type">TYPE I, II, III &nbsp;| UNFLAVOURED</p>
    <p class="product-serving">30 SERVINGS &nbsp;| &nbsp;FOOD SUPPLEMENT</p>

    <div class="leaf-strip" role="img" aria-label="Watercolour green leaves along the base of the pouch"></div>
    <div class="mushroom-art" role="img" aria-label="Watercolour oyster mushroom cluster"></div>

    <span class="badge badge--a"></span>
    <span class="badge badge--b"></span>
    <span class="badge badge--c"></span>
    <span class="badge badge--d"></span>

    <footer class="footer-band">
      <span class="footer-band__weight">NET WT 360g</span>
    </footer>
  </main>
</body>
</html>
```